Hair & Skin Product Line

I need someone to design clear product labels that can go on pink bottles. I'm looking for someone who can add graphics such as avocado and honey to the label as these are ingredients in our products. The colors we want incorporated are gold, blue, white and purple. I will upload information about our company identity and information on one label. Whoever we choose, we will use them to create 11 more labels.

Target Market(s)

Woman 25-50, Natural, straight or curly hair.

Industry/Entity Type

Beauty

```html
<!DOCTYPE html>
<html lang="en">
<head>
<meta charset="utf-8">
<title>Petal &amp; Grove – Avocado &amp; Honey Shampoo Label</title>
<link rel="stylesheet" href="https://fonts.googleapis.com/css2?family=Montserrat:ital,wght@0,400;0,500;0,600;0,700;1,500;1,600&family=Raleway:ital,wght@0,300;0,400;0,500;1,400&display=swap">
<style>
  :root{
    --page:#d7cdd0;
    --sky:#a9d1f0;
    --gold:#e8c547;
    --gold-deep:#c99a1e;
    --gold-light:#fff1b3;
    --ink:#1f2430;
    --body:#2a2d36;
    --white:#ffffff;
  }
  *{margin:0;padding:0;box-sizing:border-box}
  html,body{width:1200px;height:1200px;overflow:hidden;background:var(--page)}
  .canvas{position:relative;width:1200px;height:1200px}
  .label{
    position:absolute;left:232px;top:40px;width:545px;height:830px;
    transform:scale(1.35);transform-origin:0 0;
    font-family:"Raleway",sans-serif;color:var(--body);
  }
  .label-art{position:absolute;inset:0;width:545px;height:830px}
  .abs{position:absolute}

  /* front panel */
  .brand-name{left:20px;top:84px;width:220px;font-family:"Montserrat",sans-serif;font-weight:500;font-size:17px;color:var(--white);text-align:center;letter-spacing:.5px}
  .tagline{left:22px;top:470px;transform:rotate(-90deg);transform-origin:0 0;white-space:nowrap;font-family:"Montserrat",sans-serif;font-style:italic;font-weight:500;font-size:11.5px;color:var(--ink)}
  .product-title{left:48px;top:144px;font-family:"Montserrat",sans-serif;font-weight:600;font-size:37px;line-height:37px;color:var(--ink);letter-spacing:.3px}
  .product-type{left:48px;top:222px;font-family:"Montserrat",sans-serif;font-weight:400;font-size:19.5px;line-height:27px;color:var(--ink)}
  .hero-image{left:52px;top:282px;width:185px;height:185px;border-radius:40% 45% 50% 40%;background:radial-gradient(circle at 70% 65%,#6f9a3a 0 30%,transparent 55%),linear-gradient(140deg,#f2b23a,#e9a12a 45%,#5f8f32);opacity:.95}
  .infused-band{left:27px;top:490px;width:235px;height:72px;background:linear-gradient(90deg,var(--gold-deep),var(--gold-light) 30%,var(--gold) 60%,var(--gold-light) 85%,var(--gold-deep));display:flex;flex-direction:column;justify-content:center;align-items:center;font-family:"Raleway",sans-serif;font-size:20px;line-height:28px;color:var(--ink)}
  .benefit{left:20px;top:598px;width:250px;font-size:21px;line-height:30px;color:var(--ink);text-align:center}
  .volume{left:33px;top:760px;width:218px;height:50px;border:2px solid var(--gold);display:flex;align-items:center;justify-content:center;font-size:19px;color:var(--ink)}

  /* back panel */
  .claim{left:282px;top:20px;width:246px;font-family:"Montserrat",sans-serif;font-weight:500;font-size:14.5px;line-height:24px;color:var(--ink);text-align:center}
  .back-copy{left:282px;top:144px;width:240px;font-size:11.8px;line-height:16.4px;color:var(--body);text-align:center}
  .back-copy h3{font-family:"Montserrat",sans-serif;font-weight:600;font-size:11.5px;line-height:15px;color:var(--ink)}
  .back-copy p{margin-bottom:16px}
  .back-copy .signoff{margin-bottom:12px}
  .back-copy .names{font-family:"Montserrat",sans-serif;font-weight:600;font-style:italic}
  .back-copy .caution{font-style:italic;margin-bottom:20px}
  .back-copy .caution b{font-family:"Montserrat",sans-serif;font-weight:600}
  .website{left:264px;top:776px;width:272px;font-family:"Montserrat",sans-serif;font-weight:600;font-size:16px;color:var(--ink);text-align:center}
</style>
</head>
<body>
<div class="canvas">
  <div class="label">
    <svg class="label-art" viewBox="0 0 545 830" aria-hidden="true">
      <defs>
        <linearGradient id="goldLine" x1="0" y1="0" x2="1" y2="1">
          <stop offset="0" stop-color="#c99a1e"/>
          <stop offset=".4" stop-color="#fff1b3"/>
          <stop offset=".7" stop-color="#e8c547"/>
          <stop offset="1" stop-color="#c99a1e"/>
        </linearGradient>
      </defs>
      <path d="M2,30 Q130,10 265,22 L268,120 C272,300 150,410 30,470 L2,495 Z" fill="var(--sky)"/>
      <path d="M2,30 Q130,10 255,18 C268,24 276,60 272,120 C268,300 150,410 40,468 C20,480 8,500 6,520 L6,830" fill="none" stroke="url(#goldLine)" stroke-width="4"/>
      <rect x="260" y="5" width="282" height="122" fill="var(--sky)"/>
      <path d="M260,5 C266,60 268,100 300,118 C380,126 470,112 542,132" fill="none" stroke="url(#goldLine)" stroke-width="4"/>
      <line x1="300" y1="802" x2="500" y2="800" stroke="url(#goldLine)" stroke-width="3"/>
    </svg>

    <div class="abs brand-name">Petal &amp; Grove</div>
    <div class="abs tagline">Your only limit is the one you set for yourself!</div>
    <div class="abs product-title">AVOCADO<br>&amp; HONEY</div>
    <div class="abs product-type">MOISTURE REPAIR<br>SHAMPOO</div>
    <div class="abs hero-image" role="img" aria-label="Illustration of golden honeycomb with a halved avocado"></div>
    <div class="abs infused-band"><span>Infused With</span><span>BIOTIN + ROSEMARY</span></div>
    <div class="abs benefit">Gently cleanses<br>and hydrates for<br>retention, moisture<br>and softness</div>
    <div class="abs volume">300 ML /10 FL OZ</div>

    <div class="abs claim">This healthy paraben free<br>shampoo removes buildup<br>without feeling stripped of<br>hair’s natural oil.</div>
    <div class="abs back-copy">
      <h3>HOW TO ENJOY</h3>
      <p>Use in the shower on wet hair. Apply throughout the length of hair. For thicker textures, section first before applying to ensure every strand is penetrated. Using fingers or palms massage to emulsify with water until hair is clean. Follow with your favorite Petal &amp; Grove Conditioning treatment.</p>
      <p>Developed by a mother and daughter who love every curl!</p>
      <p class="signoff">XOXO<br><span class="names">Mara &amp; Lena</span></p>
      <h3>INGREDIENTS:</h3>
      <p>Organic Aloe Vera Juice, Cocamido­propyl Betaine, Decyl Glucoside, Sodium Lauryl Lactylate, Kosher Vegetable Glycerin, Castor Oil, Olive Oil, dl-Panthenol, Polyquart 10, Ethylhexylglycerin, Phenoxyethanol (Eco-certified, gentle, paraben free preservative), Biotin, Honey, Avocado Oil, Rosemary Essential Oil, Peppermint Essential Oil, Fragrance.</p>
      <p class="caution"><b>Caution:</b> For external use only. Avoid eye contact. Keep out of reach of children.</p>
      <p>MADE IN THE USA<br>Distr. By: Petal &amp; Grove.<br>Millbrook, DE</p>
    </div>
    <div class="abs website">PetalAndGrove.com</div>
  </div>
</div>
</body>
</html>
```